One page site for a home improvement construction company

Looking for a nice, SEO-friendly, single page site for a local handyman. Here's a good example of a similar site: https://pelvoritbuildersnv.com/

My handyman client has many photos of projects (included), so we'd like a nice photo gallery, along with the usual stuff: google map embed, nice contact form (use Elementor native), maybe a place for a few inspirational quotes.

Important: we don't want to use anything other than Elementor Pro and (maybe) a few free plugins to do your design.

Name of business is “Dorian Welkast Home Improvement”

Target Market(s)

Homeowners in upscale communities

Coding

Coded - Design and coding required

Number of Pages Required

1 page

Font styles to use
Serif
Sans Serif

Requirements
Must have
• Must be Built in Elementor. Needs a photo gallery (project portfolio) section with supplied photos.
Nice to have
• A place for an inspirational quote
Should not have
• The top photo should not be Dorian, it should be about the work.

```html
<!DOCTYPE html>
<html lang="en">
<head>
<meta charset="utf-8">
<title>Dorian Welkast Home Improvement</title>
<link href="https://fonts.googleapis.com/css2?family=Lato:wght@300;400;700&family=Montserrat:wght@300;400;600;700&display=swap" rel="stylesheet">
<style>
:root{
  --gold:#d29b58;
  --gold-deep:#c48944;
  --dark:#262626;
  --ink:#222;
  --text:#555;
  --white:#fff;
  --line:#9a9a9a;
}
*{margin:0;padding:0;box-sizing:border-box}
html,body{width:1200px;height:4219px;overflow:hidden;background:var(--white)}
body{position:relative;font-family:'Lato',sans-serif;color:var(--text)}
.abs{position:absolute}
.head{font-family:'Montserrat',sans-serif}

/* header */
.site-header{left:0;top:0;width:1200px;height:92px;background:var(--white)}
.logo{left:103px;top:30px;font-family:'Montserrat',sans-serif;font-size:26px;font-weight:700;color:var(--ink);letter-spacing:.5px}
.main-nav{left:463px;top:36px;display:flex;gap:37px;font-family:'Montserrat',sans-serif;font-size:14px;color:#888}
.main-nav .active{color:var(--ink);font-weight:600;position:relative}
.main-nav .active::after{content:"";position:absolute;left:50%;transform:translateX(-50%);bottom:-10px;width:26px;height:2px;background:var(--gold)}

/* hero */
.hero{left:0;top:92px;width:1200px;height:666px;background:linear-gradient(120deg,#3b2c20 0%,#7a5234 35%,#a7764a 55%,#6d6a5d 80%,#bdb7a6 100%)}
.hero-shade{left:0;top:92px;width:1200px;height:666px;background:linear-gradient(90deg,rgba(0,0,0,.45),rgba(0,0,0,.05))}
.hero-kicker{left:118px;top:306px;font-family:'Montserrat',sans-serif;font-weight:300;font-size:35px;color:var(--white)}
.hero-title{left:118px;top:352px;font-family:'Montserrat',sans-serif;font-weight:700;font-size:44px;line-height:54px;color:var(--white)}
.btn-gold{left:121px;top:470px;width:180px;height:51px;background:var(--gold);color:var(--white);font-family:'Montserrat',sans-serif;font-weight:700;font-size:16px;display:flex;align-items:center;justify-content:center}
.hero-arrow{top:370px}
.hero-edge{left:0;top:658px}

/* about */
.about-photo{left:124px;top:813px;width:395px;height:354px;background:linear-gradient(135deg,#4f6b3a,#7d8d5c 50%,#3d5268)}
.about-kicker{left:570px;top:822px;font-family:'Montserrat',sans-serif;font-weight:300;font-size:37px;color:var(--gold)}
.about-name{left:570px;top:858px;font-family:'Montserrat',sans-serif;font-weight:700;font-size:36px;color:var(--ink)}
.about-rule{left:570px;top:904px;width:48px;height:3px;background:var(--line)}
.about-copy{left:570px;top:926px;width:510px;font-size:14px;line-height:25px;color:#666}
.about-copy p+p{margin-top:10px}
.btn-outline{border:2px solid var(--gold);color:var(--gold);font-family:'Montserrat',sans-serif;font-weight:700;font-size:16px;display:flex;align-items:center;justify-content:center;background:var(--white)}
.about-btn{left:566px;top:1123px;width:183px;height:55px}
.call-icon{left:790px;top:1136px}
.call-label{left:832px;top:1124px;font-size:16px;color:#444}
.call-number{left:832px;top:1146px;font-family:'Montserrat',sans-serif;font-weight:700;font-size:21px;color:var(--gold)}

/* services */
.services-band{left:0;top:1252px}
.section-title{font-family:'Montserrat',sans-serif;font-size:38px;text-align:center;width:1200px;left:0}
.section-title strong{font-weight:700}
.section-title span{font-weight:300}
.services-title{top:1350px;color:var(--white)}
.title-rule{left:576px;width:48px;height:4px}
.service{width:300px}
.service-icon{position:absolute;left:0;top:0;width:62px;height:58px;border:2px solid rgba(255,255,255,.85);border-radius:4px}
.service-name{position:absolute;left:78px;top:0;font-family:'Montserrat',sans-serif;font-weight:700;font-size:24px;line-height:30px;color:var(--white)}
.service-desc{position:absolute;left:0;top:72px;width:270px;font-size:13px;line-height:17px;color:rgba(255,255,255,.85)}

/* quote */
.quote-bg{left:0;top:1866px;width:1200px;height:475px;background:linear-gradient(180deg,#3a3a3a,#262626)}
.quote-text{left:150px;top:2072px;width:900px;text-align:center;font-size:21px;line-height:35px;color:var(--white)}
.quote-mark{font-family:'Montserrat',sans-serif;font-weight:700;font-size:56px;color:var(--white);line-height:1}
.quote-author{left:0;top:2194px;width:1200px;text-align:center;font-weight:700;font-size:21px;color:var(--white)}

/* gallery */
.gallery-title{top:2396px;color:var(--ink)}
.tile{position:absolute}
.view-btn{left:514px;top:3389px;width:172px;height:54px}

/* contact */
.map{left:540px;top:3511px;width:660px;height:544px;background:linear-gradient(135deg,#ececec,#dcdcdc)}
.contact-band{left:0;top:3511px}
.contact-title{left:101px;top:3586px;font-family:'Montserrat',sans-serif;font-size:36px;color:var(--white)}
.contact-title span{font-weight:300}
.contact-title strong{font-weight:700}
.field{left:101px;width:437px;height:46px;border:1.5px solid rgba(255,255,255,.8);color:var(--white);font-size:15px;padding:14px 17px}
.submit{left:100px;top:3932px;width:151px;height:51px;background:#111;color:var(--white);font-family:'Montserrat',sans-serif;font-weight:700;font-size:17px;display:flex;align-items:center;justify-content:center}

/* footer */
.site-footer{left:0;top:4055px;width:1200px;height:164px;background:var(--dark)}
.footer-nav{left:106px;top:4103px;display:flex;gap:37px;font-family:'Montserrat',sans-serif;font-weight:600;font-size:15px;color:var(--white)}
.copyright{left:110px;top:4143px;font-size:14px;color:#ddd}
.social{top:4095px;width:35px;height:35px;border:1.5px solid var(--white);border-radius:50%}
</style>
</head>
<body>

<header class="abs site-header">
  <div class="abs logo">DORIAN <span style="font-weight:400">WELKAST</span></div>
  <nav class="abs main-nav">
    <span class="active">HOME</span><span>ABOUT</span><span>SERVICES</span><span>GALLERY</span><span>TESTIMONIALS</span><span>CONTACT US</span>
  </nav>
</header>

<section>
  <div class="abs hero" role="img" aria-label="Photo of a cedar pergola and fenced backyard deck beside a house"></div>
  <div class="abs hero-shade"></div>
  <div class="abs hero-kicker">RECENT WORK</div>
  <h1 class="abs hero-title">HOME IMPROVEMENT<br>CONSTRUCTION</h1>
  <div class="abs btn-gold">CONTACT US</div>
  <svg class="abs hero-arrow" style="left:30px" width="32" height="40" viewBox="0 0 32 40"><polyline points="22,6 8,20 22,34" fill="none" stroke="#fff" stroke-width="5"/></svg>
  <svg class="abs hero-arrow" style="left:1138px" width="32" height="40" viewBox="0 0 32 40"><polyline points="10,6 24,20 10,34" fill="none" stroke="#fff" stroke-width="5"/></svg>
  <svg class="abs hero-edge" width="1200" height="100" viewBox="0 0 1200 100">
    <polygon points="0,60 0,100 1200,100 1200,60 600,12" fill="#262626"/>
    <polygon points="0,100 600,10 1200,100" fill="#d29b58"/>
    <polygon points="0,100 600,17 1200,100" fill="#fff"/>
  </svg>
</section>

<section>
  <div class="abs about-photo" role="img" aria-label="Portrait photo of Dorian Welkast outdoors"></div>
  <div class="abs about-kicker">ABOUT</div>
  <h2 class="abs about-name">DORIAN WELKAST</h2>
  <div class="abs about-rule"></div>
  <div class="abs about-copy">
    <p>Altricies orci ac feugiat suscipit leo massa sodales velit et scelerisque mi tortor at ipsum Proin orci odio commodo ac gravida non</p>
    <p>Aristique vel te Curabitur iaculis tempus eros Curabitur vel mi sit amet magna malesuada ultrices Ut nisi erat fermentum vel congue id euismod in elit Fusce ultricies orci ac feugiat suscipit leo massa sodales velit et scelerisque quam Curabitur vel dolor ultrices ipsum</p>
  </div>
  <div class="abs btn-outline about-btn">LEARN MORE</div>
  <svg class="abs call-icon" width="34" height="34" viewBox="0 0 24 24"><path d="M6.6 10.8c1.4 2.8 3.8 5.1 6.6 6.6l2.2-2.2c.3-.3.7-.4 1-.2 1.1.4 2.3.6 3.6.6.6 0 1 .4 1 1V20c0 .6-.4 1-1 1C10.6 21 3 13.4 3 4c0-.6.4-1 1-1h3.5c.6 0 1 .4 1 1 0 1.3.2 2.5.6 3.6.1.3 0 .7-.2 1z" fill="none" stroke="#d29b58" stroke-width="1.8"/></svg>
  <div class="abs call-label">Call Us Now</div>
  <div class="abs call-number">(610) 555 0142</div>
</section>

<section>
  <svg class="abs services-band" width="1200" height="710" viewBox="0 0 1200 710" role="img" aria-label="Gold band over a faint photo of a home exterior">
    <polygon points="0,77 600,0 1200,77 1200,631 600,704 0,631" fill="#d29b58"/>
  </svg>
  <div class="abs quote-bg" role="img" aria-label="Dark photo of a finished backyard deck"></div>
  <svg class="abs" style="left:0;top:1866px" width="1200" height="92" viewBox="0 0 1200 92"><polygon points="0,0 1200,0 1200,17 600,90 0,17" fill="#d29b58"/></svg>

  <h2 class="abs section-title services-title"><span>OUR </span><strong>SERVICE</strong></h2>
  <div class="abs title-rule" style="top:1398px;background:#fff"></div>

  <div class="abs service" style="left:141px;top:1476px"><div class="service-icon" role="img" aria-label="Bathtub icon"></div><div class="service-name">Bathroom<br>Conversions</div><div class="service-desc">Agiat in pede Fusce tellus Sed metus augue convallis et vehicula</div></div>
  <div class="abs service" style="left:491px;top:1476px"><div class="service-icon" role="img" aria-label="Floor plan icon"></div><div class="service-name">Interior<br>Design Options</div><div class="service-desc">Agiat in pede Fusce tellus Sed metus augue convallis et vehicula</div></div>
  <div class="abs service" style="left:841px;top:1476px"><div class="service-icon" role="img" aria-label="Window icon"></div><div class="service-name">Window<br>Replacement</div><div class="service-desc">Agiat in pede Fusce tellus Sed metus augue convallis et vehicula</div></div>
  <div class="abs service" style="left:141px;top:1684px"><div class="service-icon" role="img" aria-label="House icon"></div><div class="service-name">House<br>Remodels</div><div class="service-desc">Agiat in pede Fusce tellus Sed metus augue convallis et vehicula</div></div>
  <div class="abs service" style="left:491px;top:1684px"><div class="service-icon" role="img" aria-label="Kitchen icon"></div><div class="service-name">Kitchen<br>Remodels</div><div class="service-desc">Agiat in pede Fusce tellus Sed metus augue convallis et vehicula</div></div>
  <div class="abs service" style="left:841px;top:1684px"><div class="service-icon" role="img" aria-label="Drafting icon"></div><div class="service-name">Architectural<br>Options</div><div class="service-desc">Agiat in pede Fusce tellus Sed metus augue convallis et vehicula</div></div>
</section>

<section>
  <div class="abs quote-mark" style="left:126px;top:2050px">&ldquo;</div>
  <blockquote class="abs quote-text">Augiat in pede Fusce tellus Sed metus augue convallis et vehicula ut pulvinar eu ante Integer orci tellus tristique vitae consequat nec mauris viverra in gravida eu mattis in ante Morbi eget arcurmentum vel congue id euismod in elit Fusce</blockquote>
  <div class="abs quote-mark" style="left:948px;top:2142px">&rdquo;</div>
  <div class="abs quote-author">By Author Name</div>
</section>

<section>
  <h2 class="abs section-title gallery-title"><span>OUR </span><strong>GALLERY</strong></h2>
  <div class="abs title-rule" style="top:2450px;background:var(--gold)"></div>

  <div class="tile" style="left:85px;top:2496px;width:337px;height:216px;background:linear-gradient(135deg,#5a5147,#7b6e60)" role="img" aria-label="Weathered wooden deck boards"></div>
  <div class="tile" style="left:85px;top:2734px;width:337px;height:268px;background:linear-gradient(135deg,#4a3b2e,#1f6fd6 40%,#2a86e8)" role="img" aria-label="Blue pool beside a railing"></div>
  <div class="tile" style="left:85px;top:3022px;width:337px;height:322px;background:linear-gradient(160deg,#8a8f6a,#5a4a3c 55%,#3e332a)" role="img" aria-label="Wide wooden deck with railing overlooking trees"></div>

  <div class="tile" style="left:442px;top:2496px;width:337px;height:316px;background:linear-gradient(135deg,#3b3b3b,#8a8580 55%,#7aa1d0)" role="img" aria-label="Stucco wall and roof corner of a shed"></div>
  <div class="tile" style="left:442px;top:2837px;width:337px;height:216px;background:linear-gradient(135deg,#9a4b3b,#7c3a2f)" role="img" aria-label="Freshly stained red wooden deck"></div>
  <div class="tile" style="left:442px;top:3071px;width:337px;height:273px;background:linear-gradient(180deg,#6f88a8,#b08a5e 45%,#8b6a45)" role="img" aria-label="New wooden steps and deck with hills behind"></div>

  <div class="tile" style="left:799px;top:2496px;width:337px;height:216px;background:linear-gradient(180deg,#8fb4d8,#b08158 50%,#7d8b5a)" role="img" aria-label="Wooden pergola beside a house"></div>
  <div class="tile" style="left:799px;top:2737px;width:337px;height:216px;background:linear-gradient(135deg,#5f5a4a,#b0754e 50%,#8a5a3a)" role="img" aria-label="New redwood deck in a garden"></div>
  <div class="tile" style="left:799px;top:2970px;width:337px;height:374px;background:linear-gradient(160deg,#8e6a4e,#6a7a5a 50%,#5a4a3e)" role="img" aria-label="Roofed shed under construction"></div>

  <div class="abs btn-outline view-btn">VIEW MORE</div>
</section>

<section>
  <div class="abs map" role="img" aria-label="Embedded street map with a location pin"></div>
  <svg class="abs contact-band" width="662" height="544" viewBox="0 0 662 544" role="img" aria-label="Gold panel over a faint photo of a pergola">
    <polygon points="0,0 562,0 660,270 562,544 0,544" fill="#d29b58"/>
  </svg>
  <h2 class="abs contact-title"><span>GET IN </span><strong>TOUCH</strong></h2>
  <div class="abs" style="left:101px;top:3634px;width:44px;height:3px;background:#fff"></div>
  <div class="abs field" style="top:3662px">Name</div>
  <div class="abs field" style="top:3719px">Email address</div>
  <div class="abs field" style="top:3778px">Phone Number</div>
  <div class="abs field" style="top:3836px;height:76px">Message</div>
  <div class="abs submit">SUBMIT</div>
</section>

<footer class="abs site-footer">
</footer>
<nav class="abs footer-nav"><span>HOME</span><span>ABOUT</span><span>SERVICES</span><span>GALLERY</span><span>TESTIMONIALS</span><span>CONTACT US</span></nav>
<div class="abs copyright">&copy; 2020 Company Name | All Rights Reserved</div>
<div class="abs social" style="left:937px" aria-label="Social link"></div>
<div class="abs social" style="left:979px" aria-label="Social link"></div>
<div class="abs social" style="left:1021px" aria-label="Social link"></div>
<div class="abs social" style="left:1063px" aria-label="Social link"></div>

</body>
</html>
```